Web Design for photo printing service

Hi
I am looking for a new web design theme for our almost ready website http://glerhorn.tqzs.net, it will soon be launched under the name: www.zuba-web.is. (ZUBA means: Zest Under Bright Arches)

This is a website focused on printing photo products like: photo books, Greeting cards, posters, etc.

The whole theme should be playful, fun, creative. The marketing will be is that Life is fun, keep your memories. remember the good time etc.

So what I am looking for is a simple, yet colorful theme, easy to use.

We will be running max 4- 6 product groups, all extra info should be on the button,
expect shopping chart and sign in should be on top.

Extra feature:
Once a year during christmas, the web will turn on christmas outfit, it transforms
to Christmas looking Web. So a X-mas version would be fun to see !

Young people 20-35, young families.

Printing

• Fun looking colorful design, simple to use.
• Dark heavy look

```html
<!DOCTYPE html>
<html lang="en">
<head>
<meta charset="utf-8">
<title>ZUBA – Photo Printing</title>
<link href="https://fonts.googleapis.com/css2?family=Montserrat:wght@400;600;700;800&display=swap" rel="stylesheet">
<style>
:root{
  --blue:#0ea0c8;
  --purple:#9b1e8a;
  --orange:#ff8a1e;
  --lime:#a3cc1a;
  --teal:#0b9a72;
  --ink:#333;
  --grey:#8a8a8a;
  --light:#b5b5b5;
  --sky:#cfe6f7;
}
*{box-sizing:border-box;margin:0;padding:0}
html,body{width:1200px;height:890px;overflow:hidden;background:#fff}
body{font-family:"Montserrat",sans-serif;color:var(--ink)}
.page{position:relative;width:1200px;height:890px;overflow:hidden;
  background:linear-gradient(180deg,var(--sky) 0%,#e6f2fb 30%,#fff 55%,#fff 100%)}
.cloud{position:absolute;border-radius:50%;background:radial-gradient(circle,#fff 55%,rgba(255,255,255,0) 72%);opacity:.85}
.brand{position:absolute;left:200px;top:22px;display:flex;align-items:center;gap:10px}
.brand-dot{width:22px;height:22px;border-radius:50%;background:var(--purple)}
.brand-name{font-size:44px;font-weight:800;color:var(--purple);letter-spacing:2px;line-height:1}
.brand-tag{position:absolute;left:232px;top:70px;font-size:9px;font-weight:600;color:var(--ink)}
.btn{position:absolute;color:#fff;font-weight:700;font-size:13px;display:flex;align-items:center;justify-content:center;border-radius:2px;box-shadow:0 2px 0 rgba(0,0,0,.12)}
.btn-login{left:813px;top:16px;width:77px;height:28px;background:linear-gradient(#ff9a2a,#f07400)}
.btn-register{left:898px;top:16px;width:101px;height:28px;background:linear-gradient(#a8d83a,#7fb81a)}
.cart{position:absolute;left:815px;top:64px;display:flex;align-items:center;gap:6px;font-size:15px;font-weight:700}
.cart span{color:var(--blue)}
.nav{position:absolute;left:200px;top:98px;width:799px;height:44px;background:linear-gradient(#fff,#f1f1f1);border:1px solid #e2e2e2;border-radius:22px;display:flex;box-shadow:0 8px 10px -6px rgba(0,0,0,.25);overflow:hidden}
.nav a{display:flex;align-items:center;justify-content:center;font-size:11.5px;font-weight:600;color:#b7b7b7;text-decoration:none;border-right:1px solid #e4e4e4;letter-spacing:-.3px}
.nav a.active{background:linear-gradient(#ff8a2c,#f46a00);color:#fff}
.nav a:last-child{border-right:0}
.hero-title{position:absolute;left:215px;top:236px;font-weight:800;letter-spacing:-1.5px;line-height:1}
.hero-title .l1{font-size:36px;color:var(--blue)}
.hero-title .l2{font-size:42px;margin-top:4px}
.c-blue{color:var(--blue)}.c-purple{color:var(--purple)}.c-lime{color:var(--lime)}.c-orange{color:var(--orange)}.c-teal{color:var(--teal)}
.btn-start{left:216px;top:323px;width:148px;height:30px;font-size:13.5px;background:linear-gradient(#a8d83a,#7fb81a)}
.collage{position:absolute;left:596px;top:146px;width:396px;height:302px;border-radius:46% 54% 50% 50%/52% 46% 54% 48%;
  background:radial-gradient(circle at 50% 50%,#6aa83a 0 22%,#3d8bc9 40%,#e7a52a 58%,#d14a2a 72%,rgba(255,255,255,0) 76%)}
.rule{position:absolute;left:200px;width:800px;height:2px;background:linear-gradient(90deg,rgba(0,0,0,0),#e6e6e6,rgba(0,0,0,0))}
.welcome{position:absolute;left:201px;top:496px}
.welcome h2{font-size:19px;font-weight:700;letter-spacing:-.8px}
.welcome .brand-name{font-size:40px;color:var(--blue)}
.welcome-row{display:flex;align-items:center;gap:8px;margin-top:6px}
.welcome-row .brand-dot{background:var(--blue);width:18px;height:18px}
.welcome-copy{position:absolute;left:381px;top:502px;width:620px;padding-left:20px;border-left:1px dotted #d5d5d5;font-size:9.6px;line-height:13px;color:var(--grey)}
.product{position:absolute;top:629px;width:170px;text-align:center}
.ring{width:102px;height:102px;margin:0 auto;border-radius:50%;border:6px solid;box-shadow:0 2px 3px rgba(0,0,0,.2)}
.ring .photo{width:100%;height:100%;border-radius:50%}
.product h3{font-size:12.5px;font-weight:400;margin-top:10px}
.product p{font-size:9.3px;line-height:12.5px;color:var(--grey);width:140px;margin:4px auto 0}
.product .more{display:block;font-size:11.5px;font-weight:600;color:#999;margin-top:10px}
.dash{position:absolute;left:200px;width:800px;border-top:1px dashed #c8c8c8}
.footer{position:absolute;top:858px;font-size:10px;color:var(--grey)}
</style>
</head>
<body>
<div class="page">
  <div class="cloud" style="left:-60px;top:150px;width:320px;height:260px"></div>
  <div class="cloud" style="left:40px;top:-60px;width:260px;height:200px"></div>
  <div class="cloud" style="left:900px;top:320px;width:360px;height:200px"></div>
  <div class="cloud" style="left:300px;top:360px;width:420px;height:160px"></div>

  <div class="brand"><span class="brand-name">ZUBA</span><span class="brand-dot"></span></div>
  <div class="brand-tag">Zest Under Bright Arches</div>

  <div class="btn btn-login">LOGIN</div>
  <div class="btn btn-register">REGISTER</div>
  <div class="cart">
    <svg width="20" height="16" viewBox="0 0 20 16"><path d="M1 4h18l-2 10H3z" fill="#333"/><path d="M6 4l3-3M14 4l-3-3" stroke="#333" stroke-width="1.6" fill="none"/><path d="M6 7v5M10 7v5M14 7v5" stroke="#fff" stroke-width="1.2"/></svg>
    MY CART: <span>0 Items</span>
  </div>

  <nav class="nav">
    <a class="active" style="width:106px">PHOTO BOOKS</a>
    <a style="width:96px">CALENDERS</a>
    <a style="width:85px">POSTERS</a>
    <a style="width:149px">OPPORTUNITIES MAP</a>
    <a style="width:172px">PRINTED PHOTOGRAPHS</a>
    <a style="width:90px">OUR PRICE</a>
    <a style="width:101px">CONTACT US</a>
  </nav>

  <h1 class="hero-title">
    <div class="l1">REMEMBER YOUR</div>
    <div class="l2"><span class="c-blue">G</span><span class="c-purple">O</span><span class="c-lime">O</span><span class="c-blue">D</span> <span class="c-orange">MEMORIES</span></div>
  </h1>
  <div class="btn btn-start">START NOW!</div>

  <div class="collage" role="img" aria-label="Fan of printed photos with a wedding group on a lawn at the centre, surrounded by colourful paint splashes"></div>

  <div class="rule" style="top:465px"></div>

  <div class="welcome">
    <h2>WELCOME TO</h2>
    <div class="welcome-row"><span class="brand-name">ZUBA</span><span class="brand-dot"></span></div>
  </div>
  <p class="welcome-copy">Lorem Ipsum is simply dummy text of the printing and typesetting industry. Lorem Ipsum has been the industry's standard dummy text ever since the 1500s, when an unknown printer took a galley of type and scrambled it to make a type specimen book. It has survived not only five centuries, but also the leap into electronic typesetting, remaining essentially unchanged. It was popularised in the 1960s with the release of Typeplate sheets containing Lorem Ipsum passages, and more recently with desktop publishing software like Pagewright Studio including versions of Lorem Ipsum.</p>

  <div class="rule" style="top:599px"></div>

  <div class="product" style="left:180px">
    <div class="ring" style="border-color:var(--blue)"><div class="photo" role="img" aria-label="Open photo book with family pictures" style="background:radial-gradient(circle,#e9d7c8,#b3483f)"></div></div>
    <h3 class="c-blue">PHOTO BOOKS</h3>
    <p>Your own photographs? Why? We know that your images deserve to...</p>
    <span class="more">More...</span>
  </div>
  <div class="product" style="left:341px">
    <div class="ring" style="border-color:var(--purple)"><div class="photo" role="img" aria-label="Stack of printed photo calendars" style="background:radial-gradient(circle,#f4f4f4,#8fb2d0)"></div></div>
    <h3 class="c-purple">CALENDERS</h3>
    <p>The calendars are uniquely funny aflestar, especially pool days...</p>
    <span class="more">More...</span>
  </div>
  <div class="product" style="left:511px">
    <div class="ring" style="border-color:var(--orange)"><div class="photo" role="img" aria-label="Collection of printed posters" style="background:radial-gradient(circle,#d8c0a0,#7a3a2a)"></div></div>
    <h3 class="c-orange">POSTERS</h3>
    <p>The posters are printed on elegant 170 gram paper. Which means...</p>
    <span class="more">More...</span>
  </div>
  <div class="product" style="left:677px">
    <div class="ring" style="border-color:var(--lime)"><div class="photo" role="img" aria-label="Folded printed maps" style="background:radial-gradient(circle,#f0f3f6,#7c9ab8)"></div></div>
    <h3 class="c-lime">OPPORTUNITIES MAP</h3>
    <p>Christmas, birthdays, confirmation, wedding or any occasion&nbsp; It's ...</p>
    <span class="more">More...</span>
  </div>
  <div class="product" style="left:843px">
    <div class="ring" style="border-color:var(--teal)"><div class="photo" role="img" aria-label="Pile of black and white printed photographs" style="background:radial-gradient(circle,#d6d6d6,#6a6a6a)"></div></div>
    <h3 class="c-teal">PRINTED PHOTOGRAPHS</h3>
    <p>Photos in all shapes and sizes printed on your convenience...</p>
    <span class="more">More...</span>
  </div>

  <div class="dash" style="top:836px"></div>
  <div class="dash" style="top:843px"></div>

  <div class="footer" style="left:201px">Privacy Policy &nbsp;-&nbsp; Terms &amp; Conditions</div>
  <div class="footer" style="right:200px">Copyright 2013 ZUBA. All Rights Reserved.</div>
</div>
</body>
</html>
```